Menu design - professional and sleek design

We need a well presented menu in MS word. Required in MS word so I can easily change and re print as required. This is very important as we change the contents quite often. Attached is the menu design, we are looking for a more sleek design. Information on the attached menu needs to be on the new design.

Requirements
Must have
• Designed to be A4 size on side so it can be folded. Very well formatted so it can be modified and added too.
Nice to have
• Some fun and creativity.

```html
<!DOCTYPE html>
<html lang="en">
<head>
<meta charset="utf-8">
<title>Marlow Kitchen — Menu</title>
<link href="https://fonts.googleapis.com/css2?family=Josefin+Sans:wght@400;600&family=Baloo+2:wght@800&display=swap" rel="stylesheet">
<style>
  :root {
    --backdrop: #d6d6d6;
    --paper: #ffffff;
    --ink: #111111;
    --cream: #f6f0d6;
  }
  * { box-sizing: border-box; margin: 0; padding: 0; }
  html, body {
    width: 1056px; height: 1200px; overflow: hidden;
    background: var(--backdrop);
  }
  .menu-page {
    position: absolute; left: 104px; top: 0;
    width: 848px; height: 1200px;
    background: var(--paper);
    color: var(--ink);
    font-family: "Josefin Sans", sans-serif;
  }
  .brand-name {
    position: absolute; left: 0; right: 0; top: 72px;
    text-align: center;
    font-family: "Josefin Sans", sans-serif;
    font-size: 66px; line-height: 1; font-weight: 600;
    letter-spacing: 1px;
    color: var(--ink);
  }
  .menu-rule {
    position: absolute; top: 192px; height: 12px;
    border-top: 2px solid var(--ink); border-bottom: 2px solid var(--ink);
  }
  .menu-rule.left { left: 70px; width: 270px; }
  .menu-rule.right { left: 509px; width: 269px; }
  .menu-badge {
    position: absolute; left: 345px; top: 163px; width: 158px; height: 67px;
    border: 2px solid var(--ink); border-radius: 14px;
    display: flex; align-items: center; justify-content: center;
    font-family: "Josefin Sans", sans-serif; font-weight: 400;
    font-size: 38px; letter-spacing: 3px; padding-top: 7px; padding-left: 3px;
  }
  .column-divider {
    position: absolute; left: 419px; top: 291px; width: 2px; height: 608px;
    background: var(--ink);
  }
  .section { position: absolute; width: 324px; }
  .section-title {
    display: block; margin: 0 auto; width: 233px; height: 33px;
    background: var(--ink); color: var(--cream);
    border-radius: 16px 18px 18px 14px;
    font-family: "Baloo 2", sans-serif; font-weight: 800;
    font-size: 21px; letter-spacing: 2px; line-height: 36px;
    text-align: center;
  }
  .item-list { list-style: none; margin-top: 24px; }
  .menu-item {
    display: flex; align-items: baseline;
    height: 37px; font-size: 19px; letter-spacing: 0.3px;
  }
  .item-leader {
    flex: 1; margin: 0 3px;
    border-bottom: 2px dotted var(--ink);
    transform: translateY(-3px);
  }
  .section.special { left: 68px; top: 302px; }
  .section.mains { left: 456px; top: 302px; }
  .section.sandwiches { left: 68px; top: 620px; }
  .section.desserts { left: 456px; top: 620px; }
  .drinks-box {
    position: absolute; left: 62px; top: 961px; width: 724px; height: 186px;
    border: 2px solid var(--ink); border-radius: 12px;
  }
  .drinks-title {
    position: absolute; left: 309px; top: 942px; width: 229px; height: 33px;
    background: var(--ink); color: var(--cream);
    border-radius: 16px 18px 18px 14px;
    font-family: "Baloo 2", sans-serif; font-weight: 800;
    font-size: 21px; letter-spacing: 3px; line-height: 36px; text-align: center;
  }
  .drinks-list {
    position: absolute; top: 994px; width: 316px; list-style: none;
  }
  .drinks-list .menu-item { height: 34px; font-size: 18px; }
  .drinks-list.left { left: 84px; }
  .drinks-list.right { left: 451px; }
  .closing-rule {
    position: absolute; left: 62px; top: 1156px; width: 724px; height: 2px;
    background: var(--ink);
  }
</style>
</head>
<body>
<main class="menu-page">
  <h1 class="brand-name">Marlow Kitchen</h1>

  <div class="menu-rule left"></div>
  <div class="menu-badge">MENU</div>
  <div class="menu-rule right"></div>

  <div class="column-divider"></div>

  <section class="section special">
    <h2 class="section-title">SPECIAL MENU</h2>
    <ul class="item-list">
      <li class="menu-item"><span>NAME OF FOOD</span><span class="item-leader"></span><span>$10</span></li>
      <li class="menu-item"><span>NAME OF FOOD</span><span class="item-leader"></span><span>$10</span></li>
      <li class="menu-item"><span>NAME OF FOOD</span><span class="item-leader"></span><span>$10</span></li>
      <li class="menu-item"><span>NAME OF FOOD</span><span class="item-leader"></span><span>$10</span></li>
      <li class="menu-item"><span>NAME OF FOOD</span><span class="item-leader"></span><span>$10</span></li>
      <li class="menu-item"><span>NAME OF FOOD</span><span class="item-leader"></span><span>$10</span></li>
    </ul>
  </section>

  <section class="section mains">
    <h2 class="section-title">MAIN DISHES</h2>
    <ul class="item-list">
      <li class="menu-item"><span>NAME OF FOOD</span><span class="item-leader"></span><span>$10</span></li>
      <li class="menu-item"><span>NAME OF FOOD</span><span class="item-leader"></span><span>$10</span></li>
      <li class="menu-item"><span>NAME OF FOOD</span><span class="item-leader"></span><span>$10</span></li>
      <li class="menu-item"><span>NAME OF FOOD</span><span class="item-leader"></span><span>$10</span></li>
      <li class="menu-item"><span>NAME OF FOOD</span><span class="item-leader"></span><span>$10</span></li>
      <li class="menu-item"><span>NAME OF FOOD</span><span class="item-leader"></span><span>$10</span></li>
    </ul>
  </section>

  <section class="section sandwiches">
    <h2 class="section-title">SANDWICHES</h2>
    <ul class="item-list">
      <li class="menu-item"><span>NAME OF FOOD</span><span class="item-leader"></span><span>$10</span></li>
      <li class="menu-item"><span>NAME OF FOOD</span><span class="item-leader"></span><span>$10</span></li>
      <li class="menu-item"><span>NAME OF FOOD</span><span class="item-leader"></span><span>$10</span></li>
      <li class="menu-item"><span>NAME OF FOOD</span><span class="item-leader"></span><span>$10</span></li>
      <li class="menu-item"><span>NAME OF FOOD</span><span class="item-leader"></span><span>$10</span></li>
      <li class="menu-item"><span>NAME OF FOOD</span><span class="item-leader"></span><span>$10</span></li>
    </ul>
  </section>

  <section class="section desserts">
    <h2 class="section-title">DESSERTS</h2>
    <ul class="item-list">
      <li class="menu-item"><span>NAME OF FOOD</span><span class="item-leader"></span><span>$10</span></li>
      <li class="menu-item"><span>NAME OF FOOD</span><span class="item-leader"></span><span>$10</span></li>
      <li class="menu-item"><span>NAME OF FOOD</span><span class="item-leader"></span><span>$10</span></li>
      <li class="menu-item"><span>NAME OF FOOD</span><span class="item-leader"></span><span>$10</span></li>
      <li class="menu-item"><span>NAME OF FOOD</span><span class="item-leader"></span><span>$10</span></li>
      <li class="menu-item"><span>NAME OF FOOD</span><span class="item-leader"></span><span>$10</span></li>
    </ul>
  </section>

  <div class="drinks-box"></div>
  <h2 class="drinks-title">DRINKS</h2>
  <ul class="drinks-list left">
    <li class="menu-item"><span>NAME OF FOOD</span><span class="item-leader"></span><span>$10</span></li>
    <li class="menu-item"><span>NAME OF FOOD</span><span class="item-leader"></span><span>$10</span></li>
    <li class="menu-item"><span>NAME OF FOOD</span><span class="item-leader"></span><span>$10</span></li>
    <li class="menu-item"><span>NAME OF FOOD</span><span class="item-leader"></span><span>$10</span></li>
  </ul>
  <ul class="drinks-list right">
    <li class="menu-item"><span>NAME OF FOOD</span><span class="item-leader"></span><span>$10</span></li>
    <li class="menu-item"><span>NAME OF FOOD</span><span class="item-leader"></span><span>$10</span></li>
    <li class="menu-item"><span>NAME OF FOOD</span><span class="item-leader"></span><span>$10</span></li>
    <li class="menu-item"><span>NAME OF FOOD</span><span class="item-leader"></span><span>$10</span></li>
  </ul>
  <div class="closing-rule"></div>
</main>
</body>
</html>
```